Flyer design for retail store owners

i would need to have a flyer design for my retail shop customers to show that I am a mailbox store that has all major shipping vendors to for their shipping needs. Ensuring that they can take advantage of opening a house account at the store and billed monthly, word document has all the details. Please use stock images for the notary public, passport photos, mailbox brass pictures of my actual mailboxes are listed in the pictures. I need to make it POP and WOW these retail store owners as I am using it to advertise the business

```html
<!DOCTYPE html>
<html lang="en">
<head>
<meta charset="utf-8">
<title>Mailbox Rental Flyer</title>
<link href="https://fonts.googleapis.com/css2?family=Montserrat:ital,wght@0,400;0,500;0,600;0,700;1,700;1,800&family=Bebas+Neue&display=swap" rel="stylesheet">
<style>
  :root{
    --brand-blue:#0f6fbb;
    --map-blue:#5a78b8;
    --ink:#1d1d1f;
    --dark-band:#252527;
    --paper:#ffffff;
    --mist:#eceef2;
    --brass:#c9975a;
    --wood:#d9bf98;
  }
  *{margin:0;padding:0;box-sizing:border-box}
  html,body{width:1200px;height:1200px;overflow:hidden;background:var(--paper)}
  body{position:relative;font-family:'Montserrat',sans-serif;color:var(--ink)}

  .page{position:absolute;top:249px;width:512px;height:723px;overflow:hidden}
  .page--front{left:86px;background:linear-gradient(180deg,var(--mist),#f7f8fa 60%,var(--mist))}
  .page--back{left:628px}

  .front__hero{position:absolute;left:0;top:0;width:512px;height:190px;
    background:linear-gradient(135deg,#4f6cae 0%,#7f97cc 45%,#5a78b8 100%)}
  .front__wave{position:absolute;left:0;top:140px;width:512px;height:420px}
  .intro{position:absolute;left:35px;top:26px;width:460px;color:#fff;font-size:11.2px;line-height:15.4px;font-weight:400}
  .intro__lead{font-weight:700;font-style:italic;font-size:14px}

  .mailbox-photo{position:absolute;left:21px;top:182px;width:226px;height:257px;
    background:linear-gradient(160deg,#dcb27a,var(--brass) 50%,#a8763e);
    border:3px solid #c9a16c}

  .promo{position:absolute;left:265px;top:233px;width:232px}
  .promo__title{font-size:19px;font-weight:700;letter-spacing:.2px;line-height:22px}
  .promo__body{font-size:9.2px;line-height:13.8px;margin-top:2px}
  .promo__body b{font-weight:600}

  .signup{position:absolute;left:256px;top:377px;width:237px;height:45px;
    border:1.5px solid var(--brand-blue);padding:2px}
  .signup__inner{width:100%;height:100%;background:var(--brand-blue);color:#fff;
    font-family:'Bebas Neue',sans-serif;font-size:21px;display:flex;align-items:center;justify-content:center;letter-spacing:-.2px}

  .deals{position:absolute;left:21px;top:458px;width:473px;height:212px}
  .deals__shape{position:absolute;inset:0}
  .deals__content{position:absolute;left:0;top:0;width:473px;color:#fff}
  .deals__title{position:absolute;left:22px;top:17px;font-size:14px;font-weight:600}
  .deals__list{position:absolute;left:11px;top:47px;width:455px;list-style:none;font-size:11px;line-height:15.4px}
  .deals__list li{padding-left:7px;text-indent:-7px;margin-bottom:5.2px}
  .deals__list li::before{content:"• ";font-size:8px}

  .offer-bar{position:absolute;left:0;top:685px;width:512px;height:38px;background:var(--dark-band);
    color:#fff;font-size:14px;font-weight:700;display:flex;align-items:center;justify-content:center}

  .back__photo{position:absolute;inset:0;background:linear-gradient(135deg,#e2caa6,var(--wood) 50%,#cdb08a)}
  .about{position:absolute;left:103px;top:192px;width:297px;height:291px;background:var(--brand-blue);
    color:#fff;padding:40px 20px 0 34px}
  .about__text{font-size:11.2px;line-height:15.45px;font-weight:600}
  .about__partners{font-size:14.5px;font-weight:800;font-style:italic;line-height:16px}
</style>
</head>
<body>
  <section class="page page--front">
    <div class="front__hero" role="img" aria-label="Blue-tinted world map with a passport and camera"></div>
    <svg class="front__wave" viewBox="0 0 512 420" preserveAspectRatio="none" aria-hidden="true">
      <path d="M0 45 C120 10 230 -10 330 18 C420 42 470 45 512 40 L512 80 C450 80 400 60 320 52 C230 45 150 70 110 100 C60 140 20 170 0 185 Z" fill="var(--dark-band)"/>
    </svg>
    <p class="intro"><span class="intro__lead">Renting a mail box</span> is one of the most efficient and cost saving methods for receiving your mail and packages. Instead of having to worry about private security, weather conditions, sorting, and deliveries; all you have to do is pick-up your mail from our secured facility each day except Sundays.&nbsp; You will get a notification when mail arrives whether envelope or package, it will be scanned in daily which other mailbox stores do not offer! We offer onsite Notary Public with no appointments and onsite Passport Photos and can ship out same day.</p>

    <div class="mailbox-photo" role="img" aria-label="Brass mailbox unit with rows of small locking doors"></div>

    <div class="promo">
      <h2 class="promo__title">MAIN PROMOTION:</h2>
      <p class="promo__body">Now renting mailboxes on Maple Grove Plaza Shopping Center. We are offering all Maple Grove Plaza shopping center owners/employees an exclusive promo deal! <b>$12 a month for 6-12 months leases! You get a mailbox in the shop, a book of stamps(20 count), 3 notarizations by appointment, 100 copies of black and white, and 100 copies of color.</b></p>
    </div>

    <div class="signup"><div class="signup__inner">PLEASE SEE ASSOCIATE FOR SIGN UP!</div></div>

    <div class="deals">
      <svg class="deals__shape" viewBox="0 0 473 212" preserveAspectRatio="none" aria-hidden="true">
        <defs>
          <linearGradient id="dealsFill" x1="0" y1="0" x2="1" y2="0">
            <stop offset="0" stop-color="#4a82c8"/>
            <stop offset=".5" stop-color="var(--brand-blue)"/>
            <stop offset="1" stop-color="var(--brand-blue)"/>
          </linearGradient>
        </defs>
        <path d="M36 0 H473 V176 L440 212 H0 V30 Z" fill="url(#dealsFill)"/>
      </svg>
      <div class="deals__content">
        <h3 class="deals__title">Check out these other deals!</h3>
        <ul class="deals__list">
          <li>As a retail owner, you know how important it is to keep your customers coming back - you will get 20% discount for printing services.</li>
          <li>We duplicate keys for $2/each, our regular price charge is $4/each. Save up to 50%!</li>
          <li>Lamination is also discounted at 10% off.</li>
          <li>10% off retail supplies ... must be minimum of 10$</li>
          <li>For house accounts -a 5% discount will be deducted monthly of billing change to invoicing PLUS we're giving another 5% of the discount if you upgrade and sign up for mailbox. Great right?</li>
        </ul>
      </div>
    </div>

    <div class="offer-bar">Take advantage of this limited time offer now!</div>
  </section>

  <section class="page page--back">
    <div class="back__photo" role="img" aria-label="Wall of numbered wooden post office boxes"></div>
    <div class="about">
      <p class="about__text">At Swift Parcel &amp; Post, our goal is to make your shipping experience as convenient as possible. Whether you are shipping packages, documents, or packages, we are here to help. Whether you want to track your package or estimate the price of your package, it is easy for you. We are ready to handle all of your postal services! Get also the services you need; printing, copying, and stop in to purchase postage or shipping materials.<br>Service point partners are</p>
      <p class="about__partners">ParcelJet, ShipRight, PostLine, and GlobeEx.</p>
    </div>
  </section>
</body>
</html>
```